Email signatures and letterhead for in-house lawyers and staff

I need Word, Outlook, and Gmail compatible letterhead and email signature block for an in-house litigation group. Simple and generic is the goal! The design must be user-modifiable for several locations and job titles. The design will work best if created in MS Word. We are an in-house group of trial lawyers, about 40 persons total, operating from nine locations, and providing services in ten US states. Letterhead will be used in header of MSWord documents. Email sig will be used in both Outlook and Gmail. The office name will be different in each of our locations, so the design has to be user-modifiable.

Industry/Entity Type

Law Firm

Font styles to use
Sans Serif

Requirements
Must have
• A fresher, more professional look than the screenshots I've posted

The screenshot with multiple attorney names in the office is most representative of the info we want included.
Nice to have
• Sylish but not overly so. Generic legal symbols might be appropriate, but can't look like tired old clip art.
Should not have
• watermarks

```html
<!DOCTYPE html>
<html lang="en">
<head>
<meta charset="utf-8">
<title>Law Office Letterhead</title>
<link href="https://fonts.googleapis.com/css2?family=Lato:wght@400;700&family=Fira+Sans+Condensed:wght@300&display=swap" rel="stylesheet">
<style>
  :root {
    --backdrop: #e4e4e4;
    --paper: #ffffff;
    --ink: #4a4a4a;
    --ink-soft: #555555;
    --band-dark: #0d0d0d;
    --band-grey: #7a7a7a;
    --signature-tone: #d9d9d9;
  }
  html, body {
    margin: 0;
    padding: 0;
    width: 1056px;
    height: 1200px;
    overflow: hidden;
    background: var(--backdrop);
  }
  .letter {
    position: absolute;
    left: 118px;
    top: 20px;
    width: 820px;
    height: 1160px;
    background: var(--paper);
    color: var(--ink);
    overflow: hidden;
  }
  .letterhead {
    position: absolute;
    top: 43px;
    left: 0;
    width: 100%;
    text-align: center;
    font-family: "Lato", sans-serif;
    color: var(--ink);
    font-size: 15px;
    line-height: 23.5px;
  }
  .letterhead p { margin: 0; }
  .letterhead .office-name {
    font-weight: 700;
    font-size: 19px;
    line-height: 23.5px;
  }
  .letterhead .contact strong { font-weight: 700; }
  .letterhead .divider { margin: 0 7px; }
  .letter-body {
    position: absolute;
    left: 79px;
    width: 665px;
    top: 358px;
    font-family: "Fira Sans Condensed", sans-serif;
    font-weight: 300;
    font-size: 18px;
    line-height: 28.5px;
    color: var(--ink-soft);
    text-align: justify;
  }
  .letter-body p { margin: 0 0 28px; }
  .letter-body .salutation { margin-bottom: 25px; }
  .closing {
    position: absolute;
    left: 79px;
    top: 928px;
    font-family: "Fira Sans Condensed", sans-serif;
    font-weight: 300;
    font-size: 18px;
    line-height: 28px;
    color: var(--ink-soft);
    margin: 0;
  }
  .signature {
    position: absolute;
    left: 78px;
    top: 966px;
    width: 80px;
    height: 44px;
    background: linear-gradient(90deg, var(--signature-tone), #f2f2f2);
    border-radius: 3px;
  }
  .footer-band {
    position: absolute;
    left: 0;
    bottom: 0;
    width: 820px;
    height: 29px;
    background: linear-gradient(180deg, var(--band-grey) 0%, var(--band-dark) 70%);
  }
</style>
</head>
<body>
  <main class="letter">
    <header class="letterhead">
      <p>Law Office of</p>
      <p class="office-name">Daniel R. Hartley</p>
      <p>4150 Meridian Ave, Suite 310</p>
      <p>Anytown, XY 99999</p>
      <p class="contact"><strong>P:</strong> (555) 204-3180<span class="divider">|</span><strong>F:</strong> (555) 204-3190</p>
    </header>

    <section class="letter-body">
      <p class="salutation">Dear Sir/Mam,</p>
      <p>Contrary to popular belief, Lorem Ipsum is not simply random text. It has roots in a piece of classical Latin literature from 45 BC, making it over 2000 years old. Harold Whitcombe, a Latin professor at Ashford College in Virginia, looked up one of the more obscure Latin words, consectetur.</p>
      <p>Lorem Ipsum comes from sections 1.10.32 and 1.10.33 of "de Finibus Bonorum et Malorum" (The Extremes of Good and Evil) by Aurelius, written in 45 BC. This book is a treatise on the theory of ethics, very popular during the Renaissance. The first line of Lorem Ipsum.</p>
      <p>The standard chunk of Lorem Ipsum used since the 1500s is reproduced below for those interested. Sections 1.10.32 and 1.10.33 from "de Finibus Bonorum et Malorum" by Aurelius are also reproduced in their exact original.</p>
      <p>The standard chunk of Lorem Ipsum used since the 1500s is reproduced below for those interested.</p>
    </section>

    <p class="closing">Best Regards</p>
    <div class="signature" role="img" aria-label="Handwritten signature of Daniel"></div>

    <div class="footer-band" role="img" aria-label="Decorative footer band in grey and black"></div>
  </main>
</body>
</html>
```